Lorna Vee Tresses Fancy Business Card’s

I want my business cards to be elite, original and very classy. I want the business cards to match the colors of my logo and to match the design posted. I would love the design of the picture I posted

I want the card all white .
The dripping on the top of the card I want it to match the pink color in my logo that’s also posted .
I need my logo on the business card !
I need my Instagram- @lorna.vee.tresses__
And my phone number - 555 207 9362

Target Market(s)

My target market is young woman age 23 to older woman to the age of 65
I want both older and younger women to love my design . I don’t want any cheap looking business cards

Industry/Entity Type

Hair And Beauty

Contact Information for Business Card

Add my logo
Add my Instagram- @lorna.vee.tresses__
My number - 555 207 9362
My website- www.lornaveetresses-example.com

Font styles to use
Serif
Script

Colors
ffffff
e667a6
e34298

Requirements
Must have
• The business cards must have my logo, my number , my website, and my Instagram!
Nice to have
• Nice to have glitter words that match my logo
• The business cards must look classy and mature
• I want them to be very unique!!
Should not have
• Should not have any colors that doesn’t match my logo ! This is very important! Please

```html
<!DOCTYPE html>
<html lang="en">
<head>
<meta charset="utf-8">
<title>Lorna Vee Tresses – Business Card</title>
<link href="https://fonts.googleapis.com/css2?family=Roboto:wght@300;400&display=swap" rel="stylesheet">
<style>
  :root {
    --white: #ffffff;
    --pink-light: #e667a6;
    --pink-deep: #e34298;
    --text-grey: #8e8e90;
    --silver-light: #d9d9db;
    --silver-dark: #7d7e81;
    --stage-top: #ffffff;
    --stage-bottom: #96979a;
  }
  * { margin: 0; padding: 0; box-sizing: border-box; }
  html, body { width: 1200px; height: 1200px; overflow: hidden; }
  body {
    background: linear-gradient(180deg, var(--stage-top) 0%, #cfd0d2 45%, var(--stage-bottom) 100%);
    font-family: "Roboto", Arial, sans-serif;
    position: relative;
  }
  .card {
    position: absolute;
    left: 223px;
    width: 753px;
    height: 451px;
    background: var(--white);
    box-shadow: 0 2px 6px rgba(0,0,0,0.12);
    overflow: hidden;
  }
  .card--front { top: 112px; }
  .card--back { top: 637px; }
  .card-art { position: absolute; inset: 0; width: 100%; height: 100%; }
  .brand-name {
    position: absolute;
    color: var(--pink-deep);
    font-family: "Roboto", Arial, sans-serif;
    font-weight: 400;
    text-align: center;
    line-height: 1.05;
    letter-spacing: 0.04em;
    transform: translate(-50%, -50%);
    white-space: nowrap;
  }
  .card--front .brand-name { left: 376px; top: 227px; font-size: 38px; }
  .card--back .brand-name { left: 186px; top: 227px; font-size: 32px; }
  .contact-list {
    list-style: none;
    position: absolute;
    left: 392px;
    top: 176px;
    width: 312px;
  }
  .contact-item {
    display: flex;
    align-items: center;
    height: 38px;
    color: var(--text-grey);
    font-weight: 300;
    font-size: 17px;
    white-space: nowrap;
  }
  .contact-icon { width: 26px; height: 26px; margin-right: 16px; flex: none; }
</style>
</head>
<body>
<svg width="0" height="0" style="position:absolute">
  <defs>
    <linearGradient id="pinkBlob" x1="0" y1="0" x2="1" y2="0">
      <stop offset="0" stop-color="#f158a5"/>
      <stop offset="1" stop-color="#f17fb5"/>
    </linearGradient>
    <linearGradient id="pinkBlobRev" x1="1" y1="0" x2="0" y2="0">
      <stop offset="0" stop-color="#f158a5"/>
      <stop offset="1" stop-color="#f17fb5"/>
    </linearGradient>
    <linearGradient id="silverFrame" x1="0" y1="0" x2="1" y2="1">
      <stop offset="0" stop-color="#a9aaad"/>
      <stop offset="0.5" stop-color="#7d7e81"/>
      <stop offset="1" stop-color="#b4b5b8"/>
    </linearGradient>
  </defs>
</svg>

<section class="card card--front" aria-label="Card front">
  <svg class="card-art" viewBox="0 0 1212 726" preserveAspectRatio="none">
    <path d="M800 726 C 860 680, 960 660, 1050 665 C 1110 668, 1150 700, 1175 726 Z" fill="url(#pinkBlob)"/>
    <rect class="silver-frame" x="48" y="48" width="1121" height="636" fill="none" stroke="url(#silverFrame)" stroke-width="30" role="img" aria-label="Silver glitter frame"/>
    <path d="M0 0 H292 C 285 70, 200 120, 90 118 C 50 117, 20 115, 0 118 Z" fill="url(#pinkBlob)"/>
    <path d="M785 0 H1212 V245 C 1160 240, 1100 190, 1000 195 C 900 200, 770 200, 768 100 C 767 50, 775 20, 785 0 Z" fill="url(#pinkBlobRev)"/>
    <path d="M0 570 C 60 530, 150 520, 230 523 C 330 526, 390 560, 430 610 C 480 670, 560 700, 630 726 H0 Z" fill="url(#pinkBlob)"/>
  </svg>
  <p class="brand-name">Lorna Vee<br>Tresses</p>
</section>

<section class="card card--back" aria-label="Card back">
  <svg class="card-art" viewBox="0 0 1212 726" preserveAspectRatio="none">
    <path d="M35 726 C 120 690, 250 680, 330 690 C 380 697, 410 712, 420 726 Z" fill="url(#pinkBlob)"/>
    <rect class="silver-frame" x="48" y="48" width="1111" height="630" fill="none" stroke="url(#silverFrame)" stroke-width="30" role="img" aria-label="Silver glitter frame"/>
    <path d="M0 0 H430 C 450 80, 440 190, 340 195 C 270 198, 200 180, 130 195 C 70 208, 30 230, 0 245 Z" fill="url(#pinkBlobRev)"/>
    <path d="M918 0 H1212 V118 C 1170 118, 1120 118, 1080 118 C 1000 118, 940 80, 918 0 Z" fill="url(#pinkBlob)"/>
    <path d="M575 726 C 700 700, 770 640, 840 570 C 900 520, 1000 510, 1080 520 C 1150 530, 1190 550, 1212 560 V726 Z" fill="url(#pinkBlob)"/>
  </svg>
  <p class="brand-name">Lorna Vee<br>Tresses</p>
  <ul class="contact-list">
    <li class="contact-item contact-item--phone">
      <svg class="contact-icon" viewBox="0 0 24 24" aria-hidden="true"><path d="M6.6 3.5 L9 3 L10.5 7 L8.6 8.4 C9.6 10.8 11.8 13.2 14.8 14.9 L16.3 13 L20.5 14.8 L20 17.2 C19.6 19 18 20.2 16.2 19.8 C10 18.5 4.8 13 4 7.6 C3.7 5.5 4.8 3.9 6.6 3.5 Z" fill="none" stroke="var(--pink-deep)" stroke-width="1.8" stroke-linejoin="round"/></svg>
      <span>555 207 9362</span>
    </li>
    <li class="contact-item contact-item--social">
      <svg class="contact-icon" viewBox="0 0 24 24" aria-hidden="true"><circle cx="12" cy="12" r="10" fill="var(--pink-deep)"/></svg>
      <span>@lorna.vee.tresses__</span>
    </li>
    <li class="contact-item contact-item--web">
      <svg class="contact-icon" viewBox="0 0 24 24" aria-hidden="true"><circle cx="12" cy="12" r="10" fill="none" stroke="var(--pink-deep)" stroke-width="1.8"/><ellipse cx="12" cy="12" rx="4.5" ry="10" fill="none" stroke="var(--pink-deep)" stroke-width="1.5"/><path d="M2 12 H22 M4 7 H20 M4 17 H20" stroke="var(--pink-deep)" stroke-width="1.3"/></svg>
      <span>www.lornaveetresses-example.com</span>
    </li>
  </ul>
</section>
</body>
</html>
```